Veteran Owned General Contractor needs Bold New Business Cards

We are a service disabled veteran owned small business. We're a general contractor that specializes in excavation, underground utilities, site work, land clearing and demolition. We would like a fresh, simple, bold, new look for our business cards. We're open to ideas! We'd like to incorporate the following information on the card:

Company Name & Logo, Name of Person, Job Title, Office Phone, Fax, Cell Phone, Email Address, Website, SDVOSB

Our logo is included. We look forward to your thoughts.

Thank you!
Updates

Reason: Hello Due to the overwhelming response to this project, we are extending the deadline one time to allow for improved communication and feedback with the top candidates. We would like to thank everyone for their hard work and exceptional creativity! Thank you

Industry/Entity Type

Business

Contact Information for Business Card

Font styles to use
Sans Serif

Requirements
Nice to have
• As we are a veteran owned company, it would be nice to incorporate an American flag into the design. Maybe on the back?

```html
<!DOCTYPE html>
<html lang="en">
<head>
<meta charset="utf-8">
<title>Ridgeline Business Card</title>
<link rel="stylesheet" href="https://fonts.googleapis.com/css2?family=Open+Sans:wght@400;600;700&display=swap">
<style>
  :root {
    --backdrop: #e8e6e3;
    --card-white: #ffffff;
    --charcoal: #2e3032;
    --slate: #7d7e80;
    --green: #6cbf40;
    --text-light: #ffffff;
    --text-muted: #8a8a8a;
  }
  * { box-sizing: border-box; margin: 0; padding: 0; }
  html, body {
    width: 1200px; height: 804px; overflow: hidden;
    background: var(--backdrop);
    font-family: "Open Sans", Arial, sans-serif;
  }
  .canvas {
    position: relative; width: 1200px; height: 804px;
    display: flex; justify-content: center; align-items: center; gap: 60px;
  }
  .card {
    position: relative; width: 320px; height: 560px; overflow: hidden;
    box-shadow: 0 6px 18px rgba(0,0,0,0.18);
  }

  /* Front */
  .card-front { background: var(--card-white); }
  .front-edge {
    position: absolute; top: 0; left: 0; right: 0; height: 10px;
    background: linear-gradient(90deg,
      var(--slate) 0 40%, var(--green) 40% 62%, var(--slate) 62% 88%, var(--green) 88% 100%);
  }
  .front-mark {
    position: absolute; top: 50%; left: 50%; transform: translate(-50%, -50%);
    display: flex; flex-direction: column; align-items: center; gap: 14px;
  }
  .front-mark .mark-square {
    width: 96px; height: 96px; background: var(--charcoal); border-radius: 6px;
  }
  .front-mark .mark-name {
    font-weight: 700; font-size: 20px; letter-spacing: 3px; color: var(--charcoal);
  }
  .front-website {
    position: absolute; top: 50%; right: 46px;
    transform: translate(50%, -50%) rotate(90deg);
    font-size: 11px; color: var(--text-muted); letter-spacing: 0.5px; white-space: nowrap;
  }

  /* Back */
  .card-back { background: var(--charcoal); display: flex; flex-direction: column; }
  .back-header {
    height: 142px; display: flex; align-items: center; justify-content: center; gap: 10px;
  }
  .back-header .brand-square { width: 26px; height: 26px; background: var(--green); border-radius: 3px; }
  .back-header .brand-name {
    font-weight: 700; font-size: 28px; letter-spacing: 4px; color: var(--green);
  }
  .band {
    display: flex; flex-direction: column; justify-content: center;
    color: var(--text-light); padding: 0 28px; margin-bottom: 5px;
  }
  .band:last-child { margin-bottom: 0; flex: 1; }
  .band-name { height: 102px; background: var(--slate); align-items: flex-end; text-align: right; }
  .band-phones { height: 100px; background: var(--green); align-items: flex-end; text-align: right; }
  .band-fax { height: 96px; background: var(--slate); align-items: flex-end; text-align: right; }
  .band-note { background: var(--green); align-items: center; text-align: center; }
  .person-name { font-size: 22px; font-weight: 400; letter-spacing: 1px; }
  .person-title { font-size: 12px; margin-top: 2px; }
  .contact-line { font-size: 14px; line-height: 1.35; }
  .tagline { font-size: 14px; line-height: 1.45; }
</style>
</head>
<body>
<main class="canvas">
  <section class="card card-front" aria-label="Business card front">
    <div class="front-edge"></div>
    <div class="front-mark">
      <div class="mark-square"></div>
      <div class="mark-name">RIDGELINE</div>
    </div>
    <div class="front-website">www.ridgelinesite.com</div>
  </section>

  <section class="card card-back" aria-label="Business card back">
    <header class="back-header">
      <div class="brand-square"></div>
      <div class="brand-name">RIDGELINE</div>
    </header>
    <div class="band band-name">
      <div class="person-name">YOUR NAME</div>
      <div class="person-title">Designation</div>
    </div>
    <div class="band band-phones">
      <div class="contact-line">+1-(123)-456-7890</div>
      <div class="contact-line">+1-(123)-456-7890</div>
    </div>
    <div class="band band-fax">
      <div class="contact-line">Fax&nbsp; +1-(123)-456-7890</div>
    </div>
    <div class="band band-note">
      <p class="tagline">Lorem Ipsum is simply<br>dummy text of the printing</p>
    </div>
  </section>
</main>
</body>
</html>
```